Brochure required for international Sports event

We need an 8 page brochure designed for an international sports event to be hosted in Japan. We are a Travel Company providing packages for participants looking to travel to the event.
The brochure will feature information on the event as well as services our company can provide.
The Brochure is to be an 8 page A4 document in portrait layout.
The brochure needs to be provided both as a print ready document and digital brochure for emailing.
Brochure structure, copy, logo and imagery has been provided
As well as a example brochure design that we like for inspiration.
Link to icons - https://www.filorabox.com/sh/qk3ramvi8ptyzel/BBBqwLpRt7VmK3H9nX2cT8gRb?dl=0
Target Market(s)
Masters/Veterans Sports Participants
Industry/Entity Type
Travel
Colors
Designer to choose colors to be used in the design.
Look and feel

```html
<!DOCTYPE html>
<html lang="en">
<head>
<meta charset="utf-8">
<title>Global Veterans Games 2021 Kansai – Travel Brochure</title>
<link href="https://fonts.googleapis.com/css2?family=Lato:wght@400;700;900&family=Oswald:wght@400;500;600&display=swap" rel="stylesheet">
<style>
:root{
  --red:#c8281e;
  --orange:#e8471c;
  --gold:#c9a53a;
  --gold-soft:#d8bd62;
  --purple:#7a2f8e;
  --blue:#1f9ad6;
  --green:#1ea24a;
  --slate:#55585e;
  --ink:#2b2b2e;
  --mist:#dde5ee;
  --panel:#e9ebee;
}
*{box-sizing:border-box;margin:0;padding:0}
html,body{width:1200px;height:3016px;overflow:hidden}
body{background:linear-gradient(180deg,#a6a8af,#8f9299);font-family:"Lato",Arial,sans-serif;color:var(--ink)}
.canvas{position:relative;width:1200px;height:3016px;overflow:hidden}
.spread{position:absolute;left:140px;width:920px;height:652px;background:#fff;overflow:hidden;box-shadow:0 10px 22px rgba(0,0,0,.28)}
.abs{position:absolute}
svg.layer{position:absolute;left:0;top:0}
.oswald{font-family:"Oswald",Arial Narrow,sans-serif}
.icon-defs{position:absolute;width:0;height:0;overflow:hidden}

.mark{position:absolute;display:flex;align-items:center;gap:5px}
.mark .dot{width:16px;height:16px;border-radius:50%;background:var(--gold);flex:none}
.mark .name{font-weight:900;font-size:8px;line-height:1.05;color:var(--purple);width:52px;text-transform:uppercase}

.hbar{position:absolute;top:20px;height:11px;font-size:7px;font-weight:700;color:#fff;line-height:11px;padding:0 6px;text-transform:uppercase}
.hbar.right{text-align:right}
.fbar{position:absolute;bottom:0;height:9px}
.pgnum{position:absolute;bottom:4px;width:26px;height:26px;border-radius:50%;background:var(--gold);color:#fff;font-size:9px;font-weight:700;text-align:center;line-height:26px}

.cover-year{left:318px;top:8px;font-weight:900;font-size:54px;color:#fff;letter-spacing:1px;line-height:1}
.cover-title{left:342px;top:62px;width:110px;text-align:center;font-weight:900;font-size:16px;line-height:1;color:#fff}
.cover-tag{left:326px;top:124px;width:126px;height:17px;background:var(--gold);color:#fff;font-size:10px;font-weight:700;text-align:center;line-height:17px}
.cover-contact{left:250px;top:510px;width:206px;text-align:right;font-size:10px;font-weight:700;color:var(--ink);line-height:1}
.cover-contact .ico{display:inline-block;width:14px;height:14px;border-radius:50%;background:var(--gold);vertical-align:middle}
.cover-contact p{margin:6px 0}
.cover-games{left:473px;top:496px;font-weight:900;font-size:27px;line-height:1.07;color:var(--ink)}
.cover-games span{color:var(--gold)}
.cover-foot{left:0;top:608px;width:920px;height:44px;background:var(--slate)}
.cover-url{left:116px;top:617px;font-size:20px;font-weight:900;color:var(--gold)}
.cover-date{left:536px;top:611px;font-size:26px;font-weight:500;color:#fff;letter-spacing:.3px}
.cover-date span{color:var(--gold)}

.h-sec{font-family:"Oswald",Arial Narrow,sans-serif;font-weight:500;font-size:17px;line-height:1;text-transform:uppercase}
.h-sec .a{color:var(--red)}
.h-sec .g{color:var(--gold)}
.h-sec .d{color:var(--ink)}
.copy{font-size:8.6px;line-height:1.33;color:#333}
.copy b{font-weight:900}
.copy .hl{color:var(--gold);font-weight:700}

.sport{position:absolute;display:flex;align-items:center;gap:8px;width:112px}
.sport .ring{width:40px;height:40px;border-radius:50%;flex:none;display:flex;align-items:center;justify-content:center;box-shadow:inset 0 0 0 2px rgba(255,255,255,.35)}
.sport .ring svg{width:24px;height:24px}
.sport span{font-size:8.5px;font-weight:700;line-height:1.1;color:#333}
.c-purple{background:var(--purple)}
.c-gold{background:var(--gold)}
.c-blue{background:var(--blue)}
.c-green{background:var(--green)}
.c-red{background:#d4242a}

.pkg{position:absolute;width:134px;height:54px;background:var(--panel);display:flex;align-items:center;gap:8px;padding-left:10px}
.pkg .ring{width:36px;height:36px;border-radius:50%;border:2px solid var(--blue);background:#fff;flex:none;display:flex;align-items:center;justify-content:center}
.pkg span{font-size:8px;font-weight:900;line-height:1.15;color:#333;text-transform:uppercase}

.map-head{left:28px;top:287px;width:402px;height:44px;background:#fff}
.map-head .t1{position:absolute;left:10px;top:6px;font-family:"Oswald",Arial Narrow,sans-serif;font-size:10px;color:var(--ink)}
.map-head .t1 span{color:var(--orange)}
.map-head .t2{position:absolute;left:34px;top:21px;font-family:"Oswald",Arial Narrow,sans-serif;font-weight:600;font-size:11px;line-height:1;color:var(--red)}
.map-head .dot{position:absolute;left:10px;top:22px;width:18px;height:18px;border-radius:50%;background:var(--gold)}

.airlines{left:16px;top:90px;width:431px;height:42px;background:#fff;box-shadow:0 2px 6px rgba(0,0,0,.25);display:flex;align-items:center;justify-content:space-around;padding:0 10px}
.airlines span{font-weight:900;font-size:13px;color:var(--ink)}
.cap{position:absolute;height:19px;color:#fff;font-size:8px;font-weight:900;text-align:center;line-height:19px;text-transform:uppercase}
.cap.red{background:var(--red)}
.cap.gold{background:var(--gold);height:16px;line-height:16px;font-size:7px}
.contact-panel{left:0;top:569px;width:460px;height:74px;background:#eceef1}
.contact-panel .mail{position:absolute;left:216px;top:-14px;width:28px;height:28px;border-radius:50%;background:var(--ink);display:flex;align-items:center;justify-content:center}
.contact-panel p{position:absolute;top:22px;width:460px;text-align:center;font-size:8.5px;color:#333}
.contact-panel .email{position:absolute;left:158px;top:38px;width:144px;height:17px;background:var(--ink);color:#fff;font-size:9px;font-weight:900;text-align:center;line-height:17px}

.schedule{left:463px;top:43px;width:356px;font-size:5px;color:#333;border:1px solid #bbb;background:#fff}
.schedule .ttl{height:10px;background:#6a6d73;color:#fff;font-weight:700;font-size:6.5px;line-height:10px;padding-left:3px}
.row{display:flex;height:10px;border-top:1px solid #d8d8d8;line-height:9px}
.row .sp{width:46px;padding-left:2px;font-weight:700;overflow:hidden;white-space:nowrap}
.row .ds{width:50px;padding-left:2px;overflow:hidden;white-space:nowrap;border-left:1px solid #d8d8d8}
.row .dates{position:relative;width:204px;border-left:1px solid #d8d8d8;background:repeating-linear-gradient(90deg,transparent 0 11px,#dedede 11px 12px)}
.row .vn{width:54px;padding-left:2px;border-left:1px solid #d8d8d8;white-space:nowrap;overflow:hidden}
.row.head{height:14px;background:#f0f0f2;font-weight:700;line-height:13px}
.row.head .dates{background:none;display:flex}
.row.head .dates b{width:12px;text-align:center;font-size:5px}
.row.head .dates b.wk{color:var(--red)}
.run{position:absolute;top:0;height:100%;left:calc(var(--s)*12px);width:calc(var(--n)*12px);background:radial-gradient(circle at 6px 50%,#e0457b 1.7px,transparent 2.3px) 0 0/12px 100% repeat-x}
.note{left:463px;top:420px;font-size:5px;color:#666}
.reg-head{left:470px;top:548px;font-family:"Oswald",Arial Narrow,sans-serif;font-size:16px;font-weight:500;color:var(--gold)}
.reg-copy{left:470px;top:584px;width:330px;font-size:7.8px;line-height:1.3;color:#333}
.reg-copy .r{color:var(--red)}
.reg-copy b{font-weight:900}
</style>
</head>
<body>
<svg class="icon-defs" aria-hidden="true">
  <defs>
    <symbol id="i-target" viewBox="0 0 24 24"><g fill="none" stroke="#fff" stroke-width="2"><circle cx="12" cy="12" r="9.5"/><circle cx="12" cy="12" r="5.5"/></g><circle cx="12" cy="12" r="2" fill="#fff"/></symbol>
    <symbol id="i-ball" viewBox="0 0 24 24"><g fill="none" stroke="#fff" stroke-width="2"><circle cx="12" cy="12" r="9.5"/><path d="M2.5 12h19M12 2.5c-4 5-4 14 0 19M12 2.5c4 5 4 14 0 19"/></g></symbol>
    <symbol id="i-trophy" viewBox="0 0 24 24"><g fill="none" stroke="#fff" stroke-width="2" stroke-linejoin="round"><path d="M7 3h10v6a5 5 0 0 1-10 0z"/><path d="M7 5H4v2a3 3 0 0 0 3 3M17 5h3v2a3 3 0 0 1-3 3M12 14v4M8 21h8"/></g></symbol>
    <symbol id="i-racket" viewBox="0 0 24 24"><g fill="none" stroke="#fff" stroke-width="2" stroke-linecap="round"><ellipse cx="10" cy="9" rx="6" ry="6.5" transform="rotate(-40 10 9)"/><path d="M14.5 14l6 6.5"/></g></symbol>
    <symbol id="i-shuttle" viewBox="0 0 24 24"><g fill="none" stroke="#fff" stroke-width="2" stroke-linejoin="round"><path d="M6 3h12l-4 13h-4z"/><circle cx="12" cy="19" r="2.5"/></g></symbol>
    <symbol id="i-wave" viewBox="0 0 24 24"><g fill="none" stroke="#fff" stroke-width="2" stroke-linecap="round"><path d="M2 15c2.5-2 5-2 7 0s5 2 7 0 4-2 6 0M2 20c2.5-2 5-2 7 0s5 2 7 0 4-2 6 0"/><circle cx="15" cy="7" r="2.5"/></g></symbol>
    <symbol id="i-boat" viewBox="0 0 24 24"><g fill="none" stroke="#fff" stroke-width="2" stroke-linejoin="round"><path d="M12 2v14H5z"/><path d="M14 5l5 11h-5M3 19h18l-2 3H5z"/></g></symbol>
    <symbol id="i-wheel" viewBox="0 0 24 24"><g fill="none" stroke="#fff" stroke-width="2" stroke-linejoin="round"><circle cx="6" cy="16" r="4"/><circle cx="18" cy="16" r="4"/><path d="M6 16l4-7h6l2 7M10 9l3 7h-7M14 5h3"/></g></symbol>
    <symbol id="i-weight" viewBox="0 0 24 24"><g fill="#fff"><rect x="2" y="8" width="3" height="8" rx="1"/><rect x="19" y="8" width="3" height="8" rx="1"/><rect x="5" y="6" width="3" height="12" rx="1"/><rect x="16" y="6" width="3" height="12" rx="1"/><rect x="8" y="11" width="8" height="2"/></g></symbol>
    <symbol id="i-tri" viewBox="0 0 24 24"><g fill="none" stroke="#fff" stroke-width="2" stroke-linejoin="round"><path d="M12 3l10 18H2z"/><path d="M7 15h10"/></g></symbol>
    <symbol id="i-pins" viewBox="0 0 24 24"><g fill="#fff"><circle cx="9" cy="15" r="6"/><path d="M17 3c1.5 0 2 1.5 1.6 3l-.6 2c1.5 2 1.5 6 .5 10h-3c-1-4-1-8 .5-10l-.6-2c-.4-1.5.1-3 1.6-3z"/></g></symbol>
    <symbol id="i-flag" viewBox="0 0 24 24"><g fill="none" stroke="#fff" stroke-width="2" stroke-linejoin="round"><path d="M5 22V3"/><path d="M5 4h13l-3 4 3 4H5"/></g></symbol>
    <symbol id="i-disc" viewBox="0 0 24 24"><g fill="none" stroke="#fff" stroke-width="2"><ellipse cx="12" cy="12" rx="10" ry="5"/><ellipse cx="12" cy="11" rx="5" ry="2"/></g></symbol>
    <symbol id="i-rope" viewBox="0 0 24 24"><g fill="none" stroke="#fff" stroke-width="2" stroke-linecap="round"><path d="M2 12c3-3 5 3 8 0s5 3 8 0 3-1 4 0"/><path d="M12 6v12"/></g></symbol>
    <symbol id="i-belt" viewBox="0 0 24 24"><g fill="none" stroke="#fff" stroke-width="2" stroke-linejoin="round"><path d="M2 9h20v4H2z"/><path d="M10 13l-3 8M14 13l3 8M10 8h4v6h-4z"/></g></symbol>
    <symbol id="i-ring" viewBox="0 0 24 24"><g fill="none" stroke="#fff" stroke-width="2"><circle cx="12" cy="12" r="9"/><circle cx="12" cy="12" r="4"/><path d="M12 3v5M12 16v5M3 12h5M16 12h5"/></g></symbol>
    <symbol id="i-club" viewBox="0 0 24 24"><g fill="none" stroke="#fff" stroke-width="2" stroke-linecap="round"><path d="M8 2l6 17"/><path d="M14 19h5"/><circle cx="6" cy="20" r="2"/></g></symbol>
  </defs>
</svg>

<div class="canvas">

<!-- ===== COVER ===== -->
<section class="spread cover" style="top:90px">
  <svg class="layer" width="920" height="652" viewBox="0 0 920 652">
    <defs>
      <linearGradient id="toriiTone" x1="0" y1="0" x2="1" y2="1">
        <stop offset="0" stop-color="#c3260f"/><stop offset=".3" stop-color="#f0561a"/><stop offset=".55" stop-color="#e03c12"/><stop offset=".75" stop-color="#9a8a80"/><stop offset="1" stop-color="#8a1e0c"/>
      </linearGradient>
      <linearGradient id="shrineTone" x1="0" y1="0" x2="0" y2="1">
        <stop offset="0" stop-color="#b9cde0"/><stop offset=".35" stop-color="#d14a2a"/><stop offset=".6" stop-color="#b8301c"/><stop offset=".8" stop-color="#9c9890"/><stop offset="1" stop-color="#6f8a4e"/>
      </linearGradient>
      <linearGradient id="headTone" x1="0" y1="0" x2="1" y2="0">
        <stop offset="0" stop-color="#c7271c"/><stop offset="1" stop-color="#ef5a1e"/>
      </linearGradient>
    </defs>
    <polygon points="330,0 760,0 920,240 920,608 760,608 500,380 360,250" fill="url(#toriiTone)" role="img" aria-label="Photo: corridor of red torii gates at a Kyoto shrine"/>
    <polygon points="0,0 640,0 360,250 0,120" fill="url(#headTone)"/>
    <polygon points="0,120 330,215 0,275" fill="var(--gold)"/>
    <polygon points="0,275 330,215 360,250 260,265 0,310" fill="var(--mist)"/>
    <polygon points="0,310 260,265 420,450 240,608 0,608" fill="url(#shrineTone)" role="img" aria-label="Photo: red shrine gate building with stone steps"/>
    <polygon points="240,608 500,380 760,608" fill="#fff"/>
    <polygon points="700,0 920,0 920,290" fill="#fff"/>
    <line x1="700" y1="0" x2="920" y2="290" stroke="var(--gold)" stroke-width="5"/>
    <line x1="500" y1="380" x2="760" y2="608" stroke="var(--gold)" stroke-width="4"/>
  </svg>
  <div class="mark" style="left:84px;top:40px"><span class="dot"></span><span class="name" style="color:var(--gold)">GVG Kansai</span></div>
  <div class="abs cover-year">2021&nbsp; 2021</div>
  <div class="abs cover-title">GLOBAL VETERANS GAMES</div>
  <div class="abs cover-tag">KANSAI-JAPAN</div>
  <div class="mark" style="left:754px;top:18px"><span class="dot" style="width:30px;height:30px"></span><span class="name" style="font-size:13px;width:100px">Global Veterans Games 2021 Kansai Japan</span></div>
  <div class="abs cover-contact">
    <p><span class="ico"></span></p>
    <p>+61 2 5550 1234</p>
    <p><span class="ico"></span></p>
    <p>hello@kansaitrip-games.com</p>
  </div>
  <div class="abs cover-games"><span>GLOBAL</span><br>VETERANS<br>GAMES</div>
  <div class="abs cover-foot"></div>
  <div class="abs cover-url">www.kansaitrip-games.com</div>
  <div class="abs cover-date oswald"><span>2021</span> MAY 14-30 - KANSAI, JAPAN</div>
</section>

<!-- ===== PAGES 2-3 ===== -->
<section class="spread" style="top:811px">
  <svg class="layer" width="920" height="652" viewBox="0 0 920 652">
    <defs>
      <linearGradient id="athleteTone" x1="0" y1="0" x2="1" y2="1">
        <stop offset="0" stop-color="#c9d8e4"/><stop offset=".3" stop-color="#9fb890"/><stop offset=".55" stop-color="#e4e04a"/><stop offset=".75" stop-color="#c48a64"/><stop offset="1" stop-color="#4f7a3e"/>
      </linearGradient>
    </defs>
    <polygon points="0,255 240,330 0,420" fill="var(--gold)"/>
    <polygon points="120,360 460,205 460,420" fill="var(--mist)"/>
    <polygon points="0,385 250,330 460,250 460,652 0,652" fill="url(#athleteTone)" role="img" aria-label="Photo: veteran runner in a yellow vest stretching on a track rail"/>
    <polygon points="300,420 460,300 460,520" fill="var(--gold)" opacity=".8"/>
    <polygon points="460,430 920,300 920,652 460,652" fill="#e6edf4"/>
  </svg>
  <div class="mark" style="left:10px;top:12px"><span class="dot"></span><span class="name">Global Veterans Games</span></div>
  <div class="hbar" style="left:100px;width:336px;background:var(--red)">The Global Veterans Games, Kansai</div>
  <div class="hbar" style="left:436px;width:53px;background:var(--gold)"></div>
  <div class="hbar right" style="left:489px;width:327px;background:var(--purple)">Sports</div>
  <div class="mark" style="left:834px;top:12px"><span class="dot"></span><span class="name">Global Veterans Games</span></div>

  <h2 class="abs h-sec" style="right:478px;top:66px"><span class="a">The Global</span> <span class="d">Veterans Games</span></h2>
  <p class="abs copy" style="left:18px;top:90px;width:424px;text-align:right">The 2021 Global Veterans Games will be the <b>10th Edition</b> of the Games and the first time it will be held in Asia. Since its inception in Toronto in 1985 the Global Veterans Games has grown to become the world's largest mass-participated international sports event. The 2021 Games will be held in the Kansai region in the west of Japan and will take place over 17 days from May 14 – 30. An estimated 50,000 participants will meet to play a total of 65 sports and explore this beautiful and alluring country.</p>
  <h2 class="abs h-sec" style="right:478px;top:158px"><span class="a">Kansai</span></h2>
  <p class="abs copy" style="left:18px;top:180px;width:424px;text-align:right">Kansai consists of seven prefectures and was formerly the political and cultural center of Japan for many centuries and includes the cities of Kyoto, Osaka, Nara and Kobe. The Kansai region is located in the center of the Japanese islands and is home to over 20 million people. The region is also host to a number of incredible sights including Osaka Castle, Fushimi Inari Shrine, Kinkaku-ji (the Golden Pavilion), Nara Deer Park, Dotonbori District Nishiki Markets and Arashiyama Bamboo Grove.</p>

  <h2 class="abs h-sec" style="left:480px;top:66px"><span class="g">Sports</span></h2>
  <p class="abs copy" style="left:480px;top:90px;width:420px">The 2021 Global Veterans Games will feature a total of <span class="hl">65 sports</span> played in first class venues across the region. The 2021 Sports include:</p>

  <div class="sport" style="left:476px;top:123px"><div class="ring c-purple"><svg><use href="#i-target"/></svg></div><span>Archery</span></div>
  <div class="sport" style="left:476px;top:179px"><div class="ring c-purple"><svg><use href="#i-flag"/></svg></div><span>Athletics</span></div>
  <div class="sport" style="left:476px;top:235px"><div class="ring c-purple"><svg><use href="#i-shuttle"/></svg></div><span>Badminton</span></div>
  <div class="sport" style="left:476px;top:291px"><div class="ring c-gold"><svg><use href="#i-ball"/></svg></div><span>Baseball</span></div>
  <div class="sport" style="left:476px;top:347px"><div class="ring c-gold"><svg><use href="#i-ball"/></svg></div><span>Basketball</span></div>
  <div class="sport" style="left:476px;top:403px"><div class="ring c-gold"><svg><use href="#i-trophy"/></svg></div><span>Canoe</span></div>
  <div class="sport" style="left:476px;top:459px"><div class="ring c-purple"><svg><use href="#i-wheel"/></svg></div><span>Cycling</span></div>
  <div class="sport" style="left:476px;top:515px"><div class="ring c-purple"><svg><use href="#i-trophy"/></svg></div><span>Dance Sports</span></div>
  <div class="sport" style="left:476px;top:571px"><div class="ring c-purple"><svg><use href="#i-trophy"/></svg></div><span>Dragonboat</span></div>

  <div class="sport" style="left:588px;top:123px"><div class="ring c-gold"><svg><use href="#i-ball"/></svg></div><span>Football</span></div>
  <div class="sport" style="left:588px;top:179px"><div class="ring c-gold"><svg><use href="#i-trophy"/></svg></div><span>Flying Disc<br>(Ultimate)</span></div>
  <div class="sport" style="left:588px;top:235px"><div class="ring c-gold"><svg><use href="#i-trophy"/></svg></div><span>Gateball</span></div>
  <div class="sport" style="left:588px;top:291px"><div class="ring c-blue"><svg><use href="#i-trophy"/></svg></div><span>Golf</span></div>
  <div class="sport" style="left:588px;top:347px"><div class="ring c-blue"><svg><use href="#i-trophy"/></svg></div><span>Handball</span></div>
  <div class="sport" style="left:588px;top:403px"><div class="ring c-blue"><svg><use href="#i-trophy"/></svg></div><span>Hockey</span></div>
  <div class="sport" style="left:588px;top:459px"><div class="ring c-gold"><svg><use href="#i-trophy"/></svg></div><span>Judo</span></div>
  <div class="sport" style="left:588px;top:515px"><div class="ring c-gold"><svg><use href="#i-belt"/></svg></div><span>Karate</span></div>
  <div class="sport" style="left:588px;top:571px"><div class="ring c-gold"><svg><use href="#i-trophy"/></svg></div><span>Lifesaving</span></div>

  <div class="sport" style="left:697px;top:123px"><div class="ring c-green"><svg><use href="#i-trophy"/></svg></div><span>Orienteering</span></div>
  <div class="sport" style="left:697px;top:179px"><div class="ring c-green"><svg><use href="#i-wave"/></svg></div><span>Rowing</span></div>
  <div class="sport" style="left:697px;top:235px"><div class="ring c-green"><svg><use href="#i-flag"/></svg></div><span>Rugby</span></div>
  <div class="sport" style="left:697px;top:291px"><div class="ring c-purple"><svg><use href="#i-boat"/></svg></div><span>Sailing</span></div>
  <div class="sport" style="left:697px;top:347px"><div class="ring c-purple"><svg><use href="#i-target"/></svg></div><span>Shooting</span></div>
  <div class="sport" style="left:697px;top:403px"><div class="ring c-purple"><svg><use href="#i-trophy"/></svg></div><span>Softball</span></div>
  <div class="sport" style="left:697px;top:459px"><div class="ring c-green"><svg><use href="#i-ball"/></svg></div><span>Soft Tennis</span></div>
  <div class="sport" style="left:697px;top:515px"><div class="ring c-green"><svg><use href="#i-racket"/></svg></div><span>Squash</span></div>
  <div class="sport" style="left:697px;top:571px"><div class="ring c-green"><svg><use href="#i-wave"/></svg></div><span>Swimming</span></div>

  <div class="sport" style="left:808px;top:123px"><div class="ring c-gold"><svg><use href="#i-trophy"/></svg></div><span>Water Polo</span></div>
  <div class="sport" style="left:808px;top:179px"><div class="ring c-gold"><svg><use href="#i-racket"/></svg></div><span>Table Tennis</span></div>
  <div class="sport" style="left:808px;top:235px"><div class="ring c-gold"><svg><use href="#i-belt"/></svg></div><span>Taekwondo</span></div>
  <div class="sport" style="left:808px;top:291px"><div class="ring c-red"><svg><use href="#i-racket"/></svg></div><span>Tennis</span></div>
  <div class="sport" style="left:808px;top:347px"><div class="ring c-red"><svg><use href="#i-pins"/></svg></div><span>Tenpin<br>Bowling</span></div>
  <div class="sport" style="left:808px;top:403px"><div class="ring c-red"><svg><use href="#i-tri"/></svg></div><span>Triathlon</span></div>
  <div class="sport" style="left:808px;top:459px"><div class="ring c-gold"><svg><use href="#i-trophy"/></svg></div><span>Tug of War</span></div>
  <div class="sport" style="left:808px;top:515px"><div class="ring c-gold"><svg><use href="#i-ball"/></svg></div><span>Volleyball</span></div>
  <div class="sport" style="left:808px;top:571px"><div class="ring c-gold"><svg><use href="#i-weight"/></svg></div><span>Weightlifting</span></div>

  <div class="fbar" style="left:0;width:460px;background:var(--red)"></div>
  <div class="fbar" style="left:460px;width:460px;background:var(--purple)"></div>
  <div class="pgnum" style="left:4px">2</div>
  <div class="pgnum" style="right:4px">3</div>
</section>

<!-- ===== PAGES 4-5 ===== -->
<section class="spread" style="top:1539px">
  <svg class="layer" width="920" height="652" viewBox="0 0 920 652">
    <defs>
      <linearGradient id="stadiumTone" x1="0" y1="0" x2="0" y2="1">
        <stop offset="0" stop-color="#2e3a2c"/><stop offset=".25" stop-color="#6f7d3c"/><stop offset=".45" stop-color="#c9d27a"/><stop offset=".6" stop-color="#7fa444"/><stop offset="1" stop-color="#2f6226"/>
      </linearGradient>
      <linearGradient id="luggageTone" x1="0" y1="0" x2="1" y2="0">
        <stop offset="0" stop-color="#2f3242"/><stop offset=".2" stop-color="#c2353e"/><stop offset=".4" stop-color="#3d4560"/><stop offset=".55" stop-color="#e0455a"/><stop offset=".75" stop-color="#d9568c"/><stop offset="1" stop-color="#4a5066"/>
      </linearGradient>
      <linearGradient id="mapTone" x1="0" y1="0" x2="1" y2="1">
        <stop offset="0" stop-color="#3aa0d8"/><stop offset=".25" stop-color="#79c04a"/><stop offset=".45" stop-color="#f2c12e"/><stop offset=".6" stop-color="#9a4ba6"/><stop offset=".8" stop-color="#f07a2a"/><stop offset="1" stop-color="#e9559a"/>
      </linearGradient>
    </defs>
    <rect x="0" y="62" width="460" height="230" fill="url(#stadiumTone)" role="img" aria-label="Photo: floodlit indoor football pitch"/>
    <polygon points="0,292 460,292 460,652 0,652" fill="#3e5566"/>
    <polygon points="300,652 460,480 460,652" fill="#5fa8d6"/>
    <rect x="28" y="331" width="402" height="307" fill="url(#mapTone)" role="img" aria-label="Venue map of the Kansai prefectures showing where each sport is held"/>
    <rect x="460" y="62" width="460" height="224" fill="url(#luggageTone)" role="img" aria-label="Photo: trolleys stacked with colourful suitcases"/>
    <polygon points="920,360 920,652 760,652" fill="#5cc4ef"/>
    <polygon points="460,652 460,560 560,652" fill="#5cc4ef"/>
  </svg>
  <div class="abs map-head">
    <div class="t1">GLOBAL VETERANS GAMES 2021 KANSAI / <span>JAPAN</span></div>
    <div class="dot"></div>
    <div class="t2">59 disciplines of 35 sports &amp;<br>Venue MAP</div>
  </div>
  <div class="mark" style="left:10px;top:12px"><span class="dot"></span><span class="name">Global Veterans Games</span></div>
  <div class="hbar" style="left:100px;width:336px;background:var(--blue)">Venue Map</div>
  <div class="hbar" style="left:436px;width:53px;background:var(--gold)"></div>
  <div class="hbar right" style="left:489px;width:327px;background:var(--green)">Tour Packages</div>
  <div class="mark" style="left:834px;top:12px"><span class="dot"></span><span class="name">Global Veterans Games</span></div>

  <h2 class="abs h-sec" style="left:483px;top:312px;font-size:20px"><span class="g">Tour</span> <span class="d">Packages</span></h2>
  <p class="abs copy" style="left:483px;top:343px;width:400px">Working with Airline and local Accommodation, Travel and Tour partners we have crafted Tour Packages with quality hotels conveniently located to the various sports venues as well as transport links. As no trip to Japan is complete without a visit to Tokyo we have included Japan's capital and some of the major sights in the package.</p>
  <h2 class="abs h-sec" style="left:483px;top:412px;font-size:20px"><span class="g">Package</span> <span class="d">Include</span></h2>

  <div class="pkg" style="left:483px;top:442px"><div class="ring"><svg width="20" height="20" viewBox="0 0 20 20"><path d="M2 11l7-2 4-7h2l-2 7 5 1v2l-5 1 2 7h-2l-4-7-7-2z" fill="var(--blue)"/></svg></div><span>Flights</span></div>
  <div class="pkg" style="left:624px;top:442px"><div class="ring"><svg width="20" height="20" viewBox="0 0 20 20"><circle cx="6" cy="5" r="2.5" fill="var(--blue)"/><circle cx="14" cy="5" r="2.5" fill="var(--blue)"/><rect x="3.5" y="9" width="5" height="9" rx="1.5" fill="var(--blue)"/><rect x="11.5" y="9" width="5" height="9" rx="1.5" fill="var(--blue)"/></svg></div><span>Meet &amp; Greet<br>with Bilingual<br>Hosts</span></div>
  <div class="pkg" style="left:763px;top:442px"><div class="ring"><svg width="20" height="20" viewBox="0 0 20 20"><rect x="2" y="5" width="16" height="9" rx="2" fill="var(--blue)"/><rect x="4" y="7" width="12" height="3" fill="#fff"/><circle cx="6" cy="15" r="1.8" fill="var(--blue)"/><circle cx="14" cy="15" r="1.8" fill="var(--blue)"/></svg></div><span>Transport</span></div>
  <div class="pkg" style="left:483px;top:504px"><div class="ring"><svg width="20" height="20" viewBox="0 0 20 20"><rect x="5" y="2" width="10" height="16" fill="var(--blue)"/><g fill="#fff"><rect x="7" y="4" width="2" height="2"/><rect x="11" y="4" width="2" height="2"/><rect x="7" y="8" width="2" height="2"/><rect x="11" y="8" width="2" height="2"/><rect x="7" y="12" width="2" height="2"/><rect x="11" y="12" width="2" height="2"/></g></svg></div><span>Accommodation</span></div>
  <div class="pkg" style="left:624px;top:504px;justify-content:center;padding:0;background:#fff"><div class="mark" style="position:static"><span class="dot"></span><span class="name" style="width:60px">Global Veterans Games Kansai</span></div></div>
  <div class="pkg" style="left:763px;top:504px"><div class="ring"><svg width="20" height="20" viewBox="0 0 20 20"><path d="M3 14V8c0-3 3-5 8-5h2c3 0 4 3 4 6v5z" fill="var(--blue)"/><rect x="5" y="6" width="7" height="3" fill="#fff"/><line x1="2" y1="17" x2="18" y2="17" stroke="var(--blue)" stroke-width="1.5"/></svg></div><span>Bullet Train</span></div>
  <div class="pkg" style="left:483px;top:565px"><div class="ring"><svg width="20" height="20" viewBox="0 0 20 20"><circle cx="10" cy="10" r="7" fill="none" stroke="var(--blue)" stroke-width="2"/><circle cx="10" cy="10" r="3.5" fill="var(--blue)"/></svg></div><span>Breakfast<br>Daily</span></div>
  <div class="pkg" style="left:624px;top:565px"><div class="ring"><svg width="20" height="20" viewBox="0 0 20 20"><circle cx="7" cy="6" r="3" fill="var(--blue)"/><rect x="3" y="10" width="8" height="8" rx="2" fill="var(--blue)"/><path d="M12 2h6v5h-3l-2 2V7h-1z" fill="var(--blue)"/></svg></div><span>Bilingual<br>Local Guides</span></div>
  <div class="pkg" style="left:763px;top:565px"><div class="ring"><svg width="20" height="20" viewBox="0 0 20 20"><circle cx="6" cy="12" r="4" fill="var(--blue)"/><circle cx="14" cy="12" r="4" fill="var(--blue)"/><rect x="4" y="4" width="4" height="6" fill="var(--blue)"/><rect x="12" y="4" width="4" height="6" fill="var(--blue)"/></svg></div><span>Sightseeing</span></div>

  <div class="fbar" style="left:0;width:460px;background:var(--blue)"></div>
  <div class="fbar" style="left:460px;width:460px;background:var(--green)"></div>
  <div class="pgnum" style="left:4px">4</div>
  <div class="pgnum" style="right:4px">5</div>
</section>

<!-- ===== PAGES 6-7 ===== -->
<section class="spread" style="top:2269px">
  <svg class="layer" width="920" height="652" viewBox="0 0 920 652">
    <defs>
      <linearGradient id="lobbyTone" x1="0" y1="0" x2="1" y2="1"><stop offset="0" stop-color="#17222e"/><stop offset=".45" stop-color="#34506a"/><stop offset=".75" stop-color="#b8a77e"/><stop offset="1" stop-color="#5c5446"/></linearGradient>
      <linearGradient id="roomTone" x1="0" y1="0" x2="1" y2="1"><stop offset="0" stop-color="#e2d4b8"/><stop offset=".5" stop-color="#a98a66"/><stop offset="1" stop-color="#4f3e30"/></linearGradient>
      <linearGradient id="buffetTone" x1="0" y1="0" x2="1" y2="1"><stop offset="0" stop-color="#3e2f27"/><stop offset=".5" stop-color="#9a7656"/><stop offset="1" stop-color="#d6b894"/></linearGradient>
      <linearGradient id="towerTone" x1="0" y1="0" x2="0" y2="1"><stop offset="0" stop-color="#d8e4ee"/><stop offset=".6" stop-color="#e9ecef"/><stop offset="1" stop-color="#6f8f68"/></linearGradient>
      <linearGradient id="crowdTone" x1="0" y1="0" x2="1" y2="0"><stop offset="0" stop-color="#262626"/><stop offset=".5" stop-color="#6a6a6a"/><stop offset=".75" stop-color="#b0b0b0"/><stop offset="1" stop-color="#3a3a3a"/></linearGradient>
    </defs>
    <polygon points="0,0 0,190 380,190" fill="var(--gold)" opacity=".85"/>
    <polygon points="0,190 380,190 460,250 460,560 0,560" fill="#fff"/>
    <rect x="19" y="198" width="207" height="158" fill="url(#lobbyTone)" role="img" aria-label="Photo: hotel lobby lounge at night"/>
    <rect x="237" y="198" width="213" height="158" fill="url(#roomTone)" role="img" aria-label="Photo: modern hotel guest room"/>
    <rect x="19" y="409" width="136" height="101" fill="url(#buffetTone)" role="img" aria-label="Photo: hotel breakfast buffet"/>
    <rect x="164" y="409" width="131" height="101" fill="url(#towerTone)" role="img" aria-label="Photo: hotel tower among city trees"/>
    <rect x="303" y="409" width="150" height="101" fill="url(#buffetTone)" role="img" aria-label="Photo: hotel restaurant food counter"/>
    <rect x="463" y="430" width="457" height="148" fill="url(#crowdTone)" role="img" aria-label="Photo: sumo wrestler in front of a crowd, black and white"/>
    <polygon points="800,430 920,430 920,520" fill="var(--gold)"/>
    <polygon points="860,530 920,470 920,578" fill="var(--gold)" opacity=".7"/>
    <rect x="460" y="578" width="460" height="74" fill="#eceef1"/>
  </svg>
  <div class="mark" style="left:10px;top:12px"><span class="dot"></span><span class="name">Global Veterans Games</span></div>
  <div class="hbar" style="left:100px;width:336px;background:var(--red)">Airline Partners &amp; Featured Hotels</div>
  <div class="hbar" style="left:436px;width:53px;background:var(--gold)"></div>
  <div class="hbar right" style="left:489px;width:327px;background:var(--purple)">Schedule</div>
  <div class="mark" style="left:834px;top:12px"><span class="dot"></span><span class="name">Global Veterans Games</span></div>

  <h2 class="abs h-sec" style="right:473px;top:66px"><span class="a">Airline</span> <span class="d">Partners</span></h2>
  <div class="abs airlines"><span>Skyhaven Air</span><span>Swiftjet</span><span>Southcross Airways</span><span>Crimson Air</span></div>
  <h2 class="abs h-sec" style="right:473px;top:170px"><span class="a">Featured</span> <span class="d">Hotels</span></h2>
  <div class="cap red" style="left:19px;top:360px;width:207px">Harbourlight Hotel, Kobe</div>
  <div class="cap red" style="left:237px;top:360px;width:213px">Hotel Kiyora, Kyoto</div>
  <div class="cap gold" style="left:19px;top:516px;width:136px">Aozora City Hotel</div>
  <div class="cap gold" style="left:164px;top:516px;width:131px">Shinjuku Meridian Hotel</div>
  <div class="cap gold" style="left:303px;top:516px;width:150px">Hotel Kiyora, Kyoto</div>
  <div class="abs contact-panel">
    <div class="mail"><svg width="14" height="10" viewBox="0 0 14 10"><rect x=".5" y=".5" width="13" height="9" fill="none" stroke="var(--gold)"/><path d="M.5 .5L7 6l6.5-5.5" fill="none" stroke="var(--gold)"/></svg></div>
    <p>For a sample package for your specific sport please contact us at</p>
    <div class="email">hello@kansaitrip-games.com</div>
  </div>

  <div class="abs schedule">
    <div class="ttl">Global Veterans Games 2021 KANSAI Sports Schedule</div>
    <div class="row head"><div class="sp">Sport</div><div class="ds">Discipline</div><div class="dates"><b>14</b><b class="wk">15</b><b class="wk">16</b><b>17</b><b>18</b><b>19</b><b>20</b><b>21</b><b class="wk">22</b><b class="wk">23</b><b>24</b><b>25</b><b>26</b><b>27</b><b>28</b><b class="wk">29</b><b class="wk">30</b></div><div class="vn">Host Venue</div></div>
    <div class="row"><div class="sp">Archery</div><div class="ds">Outdoor</div><div class="dates"><i class="run" style="--s:0;--n:3"></i></div><div class="vn">Wakayama Pref</div></div>
    <div class="row"><div class="sp">Athletics</div><div class="ds">Track &amp; Field</div><div class="dates"><i class="run" style="--s:1;--n:6"></i></div><div class="vn">Osaka City</div></div>
    <div class="row"><div class="sp">Badminton</div><div class="ds">Singles</div><div class="dates"><i class="run" style="--s:2;--n:5"></i></div><div class="vn">Kobe City</div></div>
    <div class="row"><div class="sp">Baseball</div><div class="ds">Open</div><div class="dates"><i class="run" style="--s:0;--n:8"></i></div><div class="vn">Osaka City</div></div>
    <div class="row"><div class="sp">Basketball</div><div class="ds">Open</div><div class="dates"><i class="run" style="--s:7;--n:6"></i></div><div class="vn">Hyogo Pref</div></div>
    <div class="row"><div class="sp">Canoe</div><div class="ds">Sprint</div><div class="dates"><i class="run" style="--s:3;--n:4"></i></div><div class="vn">Shiga Pref</div></div>
    <div class="row"><div class="sp">Cycling</div><div class="ds">Road Race</div><div class="dates"><i class="run" style="--s:9;--n:4"></i></div><div class="vn">Tottori Pref</div></div>
    <div class="row"><div class="sp">Dance Sports</div><div class="ds">Open</div><div class="dates"><i class="run" style="--s:11;--n:2"></i></div><div class="vn">Sakai City</div></div>
    <div class="row"><div class="sp">Dragonboat</div><div class="ds">200m</div><div class="dates"><i class="run" style="--s:4;--n:3"></i></div><div class="vn">Shiga Pref</div></div>
    <div class="row"><div class="sp">Football</div><div class="ds">Open</div><div class="dates"><i class="run" style="--s:0;--n:12"></i></div><div class="vn">Osaka City</div></div>
    <div class="row"><div class="sp">Flying Disc</div><div class="ds">Ultimate</div><div class="dates"><i class="run" style="--s:6;--n:4"></i></div><div class="vn">Kyoto Pref</div></div>
    <div class="row"><div class="sp">Gateball</div><div class="ds">Open</div><div class="dates"><i class="run" style="--s:8;--n:3"></i></div><div class="vn">Kyoto Pref</div></div>
    <div class="row"><div class="sp">Golf</div><div class="ds">Stroke</div><div class="dates"><i class="run" style="--s:2;--n:4"></i></div><div class="vn">Hyogo Pref</div></div>
    <div class="row"><div class="sp">Handball</div><div class="ds">Open</div><div class="dates"><i class="run" style="--s:10;--n:5"></i></div><div class="vn">Kobe City</div></div>
    <div class="row"><div class="sp">Hockey</div><div class="ds">Open</div><div class="dates"><i class="run" style="--s:1;--n:7"></i></div><div class="vn">Shiga Pref</div></div>
    <div class="row"><div class="sp">Judo</div><div class="ds">Kata</div><div class="dates"><i class="run" style="--s:12;--n:3"></i></div><div class="vn">Nara Pref</div></div>
    <div class="row"><div class="sp">Karate</div><div class="ds">Kumite</div><div class="dates"><i class="run" style="--s:5;--n:3"></i></div><div class="vn">Osaka City</div></div>
    <div class="row"><div class="sp">Lifesaving</div><div class="ds">Pool</div><div class="dates"><i class="run" style="--s:13;--n:3"></i></div><div class="vn">Wakayama Pref</div></div>
    <div class="row"><div class="sp">Orienteering</div><div class="ds">Forest</div><div class="dates"><i class="run" style="--s:3;--n:5"></i></div><div class="vn">Hyogo Pref</div></div>
    <div class="row"><div class="sp">Rowing</div><div class="ds">Sculls</div><div class="dates"><i class="run" style="--s:9;--n:5"></i></div><div class="vn">Shiga Pref</div></div>
    <div class="row"><div class="sp">Rugby</div><div class="ds">Sevens</div><div class="dates"><i class="run" style="--s:6;--n:4"></i></div><div class="vn">Osaka City</div></div>
    <div class="row"><div class="sp">Sailing</div><div class="ds">Dinghy</div><div class="dates"><i class="run" style="--s:11;--n:4"></i></div><div class="vn">Wakayama Pref</div></div>
    <div class="row"><div class="sp">Shooting</div><div class="ds">Rifle</div><div class="dates"><i class="run" style="--s:2;--n:5"></i></div><div class="vn">Kyoto Pref</div></div>
    <div class="row"><div class="sp">Softball</div><div class="ds">Open</div><div class="dates"><i class="run" style="--s:8;--n:6"></i></div><div class="vn">Nara Pref</div></div>
    <div class="row"><div class="sp">Soft Tennis</div><div class="ds">Doubles</div><div class="dates"><i class="run" style="--s:14;--n:3"></i></div><div class="vn">Kobe City</div></div>
    <div class="row"><div class="sp">Squash</div><div class="ds">Singles</div><div class="dates"><i class="run" style="--s:4;--n:4"></i></div><div class="vn">Osaka City</div></div>
    <div class="row"><div class="sp">Swimming</div><div class="ds">Pool</div><div class="dates"><i class="run" style="--s:10;--n:6"></i></div><div class="vn">Osaka City</div></div>
    <div class="row"><div class="sp">Table Tennis</div><div class="ds">Singles</div><div class="dates"><i class="run" style="--s:0;--n:5"></i></div><div class="vn">Kyoto Pref</div></div>
    <div class="row"><div class="sp">Taekwondo</div><div class="ds">Poomsae</div><div class="dates"><i class="run" style="--s:7;--n:3"></i></div><div class="vn">Kobe City</div></div>
    <div class="row"><div class="sp">Tennis</div><div class="ds">Singles</div><div class="dates"><i class="run" style="--s:12;--n:5"></i></div><div class="vn">Hyogo Pref</div></div>
    <div class="row"><div class="sp">Tenpin Bowling</div><div class="ds">Singles</div><div class="dates"><i class="run" style="--s:5;--n:5"></i></div><div class="vn">Sakai City</div></div>
    <div class="row"><div class="sp">Triathlon</div><div class="ds">Sprint</div><div class="dates"><i class="run" style="--s:14;--n:2"></i></div><div class="vn">Tokushima Pref</div></div>
    <div class="row"><div class="sp">Tug of War</div><div class="ds">Outdoor</div><div class="dates"><i class="run" style="--s:9;--n:3"></i></div><div class="vn">Nara Pref</div></div>
    <div class="row"><div class="sp">Volleyball</div><div class="ds">Indoor</div><div class="dates"><i class="run" style="--s:1;--n:6"></i></div><div class="vn">Osaka City</div></div>
    <div class="row"><div class="sp">Weightlifting</div><div class="ds">Open</div><div class="dates"><i class="run" style="--s:13;--n:4"></i></div><div class="vn">Kobe City</div></div>
  </div>
  <div class="abs note">* Schedule may change due to local conditions</div>

  <h2 class="abs reg-head">REGISTRATIONS</h2>
  <p class="abs reg-copy">Early entries for the Global Veterans Games will open on <b class="r">6th January 2020</b>, with full entry opening in February 2020.<br>The Registration Fee for overseas participants is <span class="r">24,000 yen/person</span><br>(Including a transportation pass for mobility within the Kansai area.)<br>For more information visit - <b>www.gvg-kansai.jp</b></p>

  <div class="fbar" style="left:0;width:460px;background:var(--red)"></div>
  <div class="fbar" style="left:460px;width:460px;background:var(--purple)"></div>
  <div class="pgnum" style="left:4px">6</div>
  <div class="pgnum" style="right:4px">7</div>
</section>

</div>
</body>
</html>
```